Painting Contractor Business Card Design

We are looking for a cool, bold, modern, polished, business card design. We are a high-end residential painting contractor. Please incorporate our logo and keep with our green/black color scheme. We are interested in seeing 2-sided and 1-sided options. Thank you very much!

Industry/Entity Type

Business

Contact Information for Business Card

Info for the card:
Owen Talsky
mobile 206-555-0193
email owen@kestrowfinish.net
web www.kestrowfinish.net

```html
<!DOCTYPE html>
<html lang="en">
<head>
<meta charset="utf-8">
<title>Kestrow Finish – Business Card</title>
<link href="https://fonts.googleapis.com/css2?family=Lato:wght@300;400;700;900&display=swap" rel="stylesheet">
<style>
  :root {
    --page: #e4e4e4;
    --white: #ffffff;
    --black: #0a0a0a;
    --ink: #3a3a3a;
    --ink-strong: #262626;
    --orange: #f15a24;
    --yellow: #f7b519;
    --green: #74b843;
    --blue: #1a7ac2;
    --navy: #0d5189;
    --brand-green: #3fae49;
    --fold: rgba(0,0,0,0.35);
  }
  * { box-sizing: border-box; margin: 0; padding: 0; }
  html, body { width: 1200px; height: 926px; overflow: hidden; }
  body {
    background: var(--page);
    font-family: "Lato", Arial, sans-serif;
    position: relative;
  }
  .card {
    position: absolute;
    left: 300px;
    width: 600px;
    height: 343px;
    overflow: hidden;
    box-shadow: 0 6px 18px rgba(0,0,0,0.18);
  }
  .card-front { top: 80px; background: var(--white); }
  .card-back { top: 503px; background: var(--white); }

  /* colour tab stacks */
  .tab-stack { position: absolute; width: 46px; display: flex; flex-direction: column; }
  .tab-stack span { display: block; height: 30px; }
  .tab-stack .t-orange { background: var(--orange); }
  .tab-stack .t-yellow { background: var(--yellow); }
  .tab-stack .t-green { background: var(--green); }
  .tab-stack .t-blue { background: var(--blue); }
  .tab-stack .t-navy { background: var(--navy); }
  .tab-stack-left { left: 0; top: 0; }
  .tab-stack-right { right: 0; top: 80px; }
  .tab-stack-right span { height: 36px; }

  .brand {
    position: absolute;
    display: flex;
    align-items: center;
    gap: 10px;
    font-weight: 900;
    letter-spacing: 2px;
    white-space: nowrap;
  }
  .brand-mark { width: 16px; height: 16px; background: var(--brand-green); }
  .card-front .brand { left: 50%; top: 50%; transform: translate(-50%, -50%); font-size: 34px; color: var(--ink-strong); }

  /* back */
  .back-panel { position: absolute; left: 0; top: 0; width: 250px; height: 100%; background: var(--black); }
  .card-back .brand {
    left: 0;
    width: 220px;
    top: 148px;
    justify-content: center;
    font-size: 15px;
    letter-spacing: 1px;
    gap: 7px;
    color: var(--brand-green);
  }
  .card-back .brand-mark { width: 10px; height: 10px; }

  .info-tab {
    position: absolute;
    left: 220px;
    width: 50px;
    height: 50px;
    display: flex;
    align-items: center;
    justify-content: center;
  }
  .info-tab::after {
    content: "";
    position: absolute;
    left: 0;
    bottom: -8px;
    border-top: 8px solid var(--fold);
    border-left: 8px solid transparent;
    display: none;
  }
  .info-tab svg { width: 24px; height: 24px; fill: none; stroke: var(--white); stroke-width: 2; }
  .tab-name { top: 40px; background: var(--orange); }
  .tab-phone { top: 150px; background: var(--green); }
  .tab-web { top: 200px; background: var(--blue); }
  .tab-mail { top: 250px; background: var(--navy); }
  .tab-mail::after, .tab-name::after { display: block; }

  .contact-line { position: absolute; left: 300px; color: var(--ink); white-space: nowrap; }
  .person-name { top: 46px; font-size: 30px; font-weight: 300; letter-spacing: 1px; color: var(--ink); }
  .person-name strong { font-weight: 900; color: var(--ink-strong); }
  .phone { top: 158px; font-size: 29px; font-weight: 400; }
  .web { top: 214px; font-size: 17px; }
  .mail { top: 264px; font-size: 17px; }
</style>
</head>
<body>

<section class="card card-front" aria-label="Business card front">
  <div class="tab-stack tab-stack-left">
    <span class="t-orange"></span><span class="t-yellow"></span><span class="t-green"></span><span class="t-blue"></span><span class="t-navy"></span>
  </div>
  <div class="brand"><span class="brand-mark"></span>KESTROW FINISH</div>
  <div class="tab-stack tab-stack-right">
    <span class="t-orange"></span><span class="t-yellow"></span><span class="t-green"></span><span class="t-blue"></span><span class="t-navy"></span>
  </div>
</section>

<section class="card card-back" aria-label="Business card back">
  <div class="back-panel"></div>
  <div class="brand"><span class="brand-mark"></span>KESTROW FINISH</div>

  <div class="info-tab tab-name">
    <svg viewBox="0 0 24 24"><circle cx="12" cy="8" r="4" fill="#fff" stroke="none"/><path d="M4 21c0-4.5 3.6-7 8-7s8 2.5 8 7z" fill="#fff" stroke="none"/></svg>
  </div>
  <div class="contact-line person-name">OWEN <strong>TALSKY</strong></div>

  <div class="info-tab tab-phone">
    <svg viewBox="0 0 24 24"><path d="M6 3h3l2 5-2 1.5a11 11 0 0 0 5.5 5.5L16 13l5 2v3a2 2 0 0 1-2 2A16 16 0 0 1 4 5a2 2 0 0 1 2-2z"/></svg>
  </div>
  <div class="contact-line phone">206-555-0193</div>

  <div class="info-tab tab-web">
    <svg viewBox="0 0 24 24"><circle cx="12" cy="12" r="9"/><path d="M3 12h18M12 3c3 3 3 15 0 18M12 3c-3 3-3 15 0 18"/></svg>
  </div>
  <div class="contact-line web">www.kestrowfinish.net</div>

  <div class="info-tab tab-mail">
    <svg viewBox="0 0 24 24"><rect x="3" y="6" width="18" height="12"/><path d="M3 6l9 7 9-7"/></svg>
  </div>
  <div class="contact-line mail">owen@kestrowfinish.net</div>
</section>

</body>
</html>
```